Childcare Centre trifold brochure

Design a contemporary trifold brochure for a childcare centre that meets Australian printing requirements with supplied content, logo's, fonts and photo's. Please refer to the attached DL flyer front and back for similar possible style and content.

Target Market(s)

Families

Industry/Entity Type

Childcare

Requirements
Must have
• refer attached content, photo's, logo's and examples. Colours should be same as Pantone purple and green and or variations of. Refer attached dl flyer example.

```html
<!DOCTYPE html>
<html lang="en">
<head>
<meta charset="utf-8">
<title>Bright Sprouts – Trifold Brochure</title>
<link href="https://fonts.googleapis.com/css2?family=Luckiest+Guy&family=Open+Sans:wght@400;600;700&display=swap" rel="stylesheet">
<style>
  :root {
    --purple: #ab1fbb;
    --purple-deep: #8e189c;
    --green: #20a53a;
    --green-deep: #178a2e;
    --ink: #1f1f1f;
    --paper: #ffffff;
    --mist: #e6e6e6;
    --stage: #dcdcdc;
  }
  * { margin: 0; padding: 0; box-sizing: border-box; }
  html, body { width: 1200px; height: 900px; overflow: hidden; }
  body { background: var(--stage); font-family: "Open Sans", Arial, sans-serif; color: var(--ink); }

  .brochure {
    position: absolute; left: 87px; top: 78px; width: 1025px; height: 744px;
    display: flex; background: var(--paper);
  }
  .panel { position: relative; height: 100%; overflow: hidden; }
  .panel--inside-left { width: 353px; }
  .panel--middle { width: 322px; }
  .panel--cover { width: 350px; }
  .panel svg.backdrop { position: absolute; inset: 0; width: 100%; height: 100%; }

  /* left panel text */
  .about { position: absolute; left: 26px; top: 45px; width: 310px; font-size: 11.2px; line-height: 1.38; text-align: justify; }
  .about p { margin-bottom: 17px; }

  /* quote */
  .quote { position: absolute; left: 16px; top: 46px; width: 290px; color: var(--paper); font-size: 11.3px; line-height: 1.36; text-align: justify; }
  .quote-author { position: absolute; top: 124px; width: 100%; text-align: center; color: var(--paper); font-weight: 700; font-size: 12.5px; }

  /* brand */
  .brand { position: absolute; width: 100%; text-align: center; }
  .brand-mark { display: inline-block; width: 16px; height: 16px; border-radius: 50%; background: var(--green); vertical-align: 3px; margin-right: 6px; }
  .brand-name { font-family: "Luckiest Guy", "Open Sans", sans-serif; color: var(--purple); letter-spacing: 0.5px; }
  .brand-tagline { color: var(--green-deep); font-weight: 700; }
  .brand--middle { top: 488px; }
  .brand--middle .brand-name { font-size: 25px; }
  .brand--middle .brand-tagline { font-size: 9.5px; margin-top: 2px; }
  .brand--cover { top: 122px; }
  .brand--cover .brand-name { font-size: 31px; }
  .brand--cover .brand-tagline { font-size: 11px; margin-top: 2px; }

  .contact { position: absolute; width: 100%; text-align: center; font-size: 11.5px; line-height: 1.3; }
  .contact--visit { top: 562px; }
  .contact-rule { position: absolute; top: 634px; left: 76px; width: 170px; height: 2px; background: #333; }
  .contact--reach { top: 650px; }

  /* cover headline */
  .cover-kicker { position: absolute; top: 612px; width: 100%; text-align: center; font-family: "Luckiest Guy", sans-serif; color: var(--green); font-size: 15.5px; letter-spacing: 0.6px; }
  .cover-title { position: absolute; top: 632px; width: 100%; text-align: center; font-family: "Luckiest Guy", sans-serif; color: var(--purple); font-size: 45px; letter-spacing: 0.5px; }
  .cover-web { position: absolute; top: 678px; width: 100%; text-align: center; color: var(--green-deep); font-weight: 700; font-size: 14.5px; letter-spacing: 2px; }
</style>
</head>
<body>
<main class="brochure">

  <!-- Inside left panel -->
  <section class="panel panel--inside-left">
    <svg class="backdrop" viewBox="0 0 353 744" preserveAspectRatio="none">
      <defs>
        <linearGradient id="leftPaper" x1="0" y1="0" x2="1" y2="0">
          <stop offset="0" stop-color="#e8e8e8"/><stop offset="0.6" stop-color="#ffffff"/><stop offset="1" stop-color="#f4f4f4"/>
        </linearGradient>
        <linearGradient id="leftPhoto" x1="0" y1="0" x2="0" y2="1">
          <stop offset="0" stop-color="#8fb0c4"/><stop offset="0.35" stop-color="#6e5a44"/><stop offset="1" stop-color="#b9a58a"/>
        </linearGradient>
      </defs>
      <rect width="353" height="744" fill="url(#leftPaper)"/>
      <path d="M0,478 C110,500 230,460 353,395 L353,744 L0,744 Z" fill="var(--green)"/>
      <path d="M0,494 C110,516 230,476 353,411 L353,744 L0,744 Z" fill="var(--purple)"/>
      <circle cx="171" cy="548" r="119" fill="var(--green)"/>
      <circle cx="171" cy="548" r="111" fill="var(--paper)"/>
      <circle cx="171" cy="548" r="104" fill="url(#leftPhoto)" role="img" aria-label="Photo of the nature playground with logs, rocks and a sandy creek bed"/>
    </svg>
    <div class="about">
      <p>We are a Reggio Emilia inspired Childcare Centre offering long day care and a Nature Kindergarten program for <strong>3 – 6-year</strong> olds.</p>
      <p>At the core of our program is a Child-First ‘emergent curriculum’. An emergent Curriculum can be defined as a way of supporting learning that is based on the children’s interests</p>
      <p>Learning occurs naturally, children thrive and learn best when their interests are considered and captured.</p>
      <p>Which means our Educators act as mentors for the children as they guide them through the adventure of learning outdoors in academic subjects such as science, technology, engineering and maths (STEM).</p>
      <p>Our children spend their days predominantly outdoors all year round in one of two-amazing large Naturescape playgrounds full of native trees, a running creek bed, large stepping logs, a herb, vegetable and bush tucker garden along with a recycled mud kitchen made by the children, worm farm, compost bin and chickens and a fire pit where the older children can cook over an open fire.</p>
    </div>
  </section>

  <!-- Middle panel -->
  <section class="panel panel--middle">
    <svg class="backdrop" viewBox="0 0 322 744" preserveAspectRatio="none">
      <defs>
        <linearGradient id="midPaper" x1="0" y1="0" x2="1" y2="0">
          <stop offset="0" stop-color="#ececec"/><stop offset="0.5" stop-color="#ffffff"/><stop offset="1" stop-color="#e9e9e9"/>
        </linearGradient>
        <linearGradient id="midPhoto" x1="0" y1="0" x2="0" y2="1">
          <stop offset="0" stop-color="#ffffff"/><stop offset="0.45" stop-color="#d7d2d8"/><stop offset="1" stop-color="#f2f2f2"/>
        </linearGradient>
      </defs>
      <rect width="322" height="744" fill="url(#midPaper)"/>
      <path d="M0,0 H322 V385 C230,388 110,415 0,452 Z" fill="var(--green)"/>
      <path d="M0,452 C110,415 230,388 322,385 L322,408 C230,410 110,440 0,482 Z" fill="var(--purple)"/>
      <circle cx="158" cy="262" r="118" fill="var(--purple)"/>
      <circle cx="158" cy="262" r="110" fill="var(--paper)"/>
      <circle cx="158" cy="262" r="104" fill="url(#midPhoto)" role="img" aria-label="Photo of a toddler in a purple hat digging in the garden"/>
    </svg>
    <p class="quote">“Passion is lifted from the earth itself by the muddy hands of the young; it travels along grass stained sleeves to the heart. If we are going to save environmentalism and the environment, we must also save an endangered indicator species: the child in nature.”</p>
    <p class="quote-author">Margaret Ellison</p>

    <div class="brand brand--middle">
      <div><span class="brand-mark"></span><span class="brand-name">Bright Sprouts</span></div>
      <div class="brand-tagline">Early Development &amp; Education Centre</div>
    </div>
    <div class="contact contact--visit">
      Opening Hours: 6:00am – 6:00pm Monday – Friday<br>
      (except public holidays)<br>
      Address: 18 Banksia Road, Wattle Grove, WA 6107<br>
      Facebook: brightsproutsOZ
    </div>
    <div class="contact-rule"></div>
    <div class="contact contact--reach">
      hello@bright-sprouts.com.au<br>
      Tel: 08 9000 4182<br>
      Web: bright-sprouts.com.au
    </div>
  </section>

  <!-- Cover panel -->
  <section class="panel panel--cover">
    <svg class="backdrop" viewBox="0 0 350 744" preserveAspectRatio="none">
      <defs>
        <linearGradient id="coverPaper" x1="0" y1="0" x2="0" y2="1">
          <stop offset="0" stop-color="#ededed"/><stop offset="0.45" stop-color="#dadada"/><stop offset="0.7" stop-color="#ffffff"/><stop offset="1" stop-color="#ffffff"/>
        </linearGradient>
        <linearGradient id="coverPhoto" x1="0" y1="0" x2="1" y2="1">
          <stop offset="0" stop-color="#f2c9b0"/><stop offset="0.5" stop-color="#e7b89d"/><stop offset="1" stop-color="#8fb4d8"/>
        </linearGradient>
      </defs>
      <rect width="350" height="744" fill="url(#coverPaper)"/>
      <path d="M0,300 C120,290 240,300 350,270 L350,296 C240,326 120,318 0,326 Z" fill="var(--green)"/>
      <path d="M0,326 C120,318 240,326 350,296 L350,380 C240,390 120,395 0,400 Z" fill="var(--purple)"/>
      <circle cx="183" cy="392" r="163" fill="var(--purple)"/>
      <circle cx="183" cy="392" r="152" fill="var(--paper)"/>
      <circle cx="183" cy="392" r="148" fill="var(--green)"/>
      <circle cx="183" cy="392" r="143" fill="url(#coverPhoto)" role="img" aria-label="Photo of a group of young children lying in a circle, smiling up at the camera"/>
    </svg>
    <div class="brand brand--cover">
      <div><span class="brand-mark"></span><span class="brand-name">Bright Sprouts</span></div>
      <div class="brand-tagline">Early Development &amp; Education Centre</div>
    </div>
    <p class="cover-kicker">Getting Ready for Kindergarten</p>
    <h1 class="cover-title">The First Step</h1>
    <p class="cover-web">www.bright-sprouts.com.au</p>
  </section>

</main>
</body>
</html>
```